Start a weight loss Clinic

build a landing page website using the content from this websites. we want to copy all the content from slimpathcoaching.net but make page look more professional. we dont have a logo yet but url is www.brightvitalitycentre.com
https://clinicwellnessalliancegroup.net/home-page
https://www.slimpathcoaching.net/

Target Market(s)

people looking to open a weightloss clinic or a franchise opportunity

Coding

Number of Pages Required

3 page

Requirements
Must have
• copy all content from other site https://www.slimpathcoaching.net/

```html
<!DOCTYPE html>
<html lang="en">
<head>
<meta charset="utf-8">
<title>Bright Vitality Centre – Start Your Own Weight Loss Clinic</title>
<link rel="stylesheet" href="https://fonts.googleapis.com/css2?family=Roboto:wght@300;400;500;700;900&display=swap">
<style>
:root{
  --teal:#17877d;
  --teal-dark:#0f6f66;
  --teal-soft:#e6f1ef;
  --ink:#2a2a2a;
  --muted:#7a7a7a;
  --line:#d9d9d9;
  --hero-bg:#eeeeef;
  --white:#ffffff;
  --black:#111111;
}
*{box-sizing:border-box;margin:0;padding:0}
html,body{width:1200px;height:2828px;overflow:hidden}
body{position:relative;font-family:"Roboto",Arial,sans-serif;color:var(--ink);background:var(--white)}
.abs{position:absolute}

/* header */
.site-header{left:0;top:0;width:1200px;height:112px;background:var(--white)}
.brand{left:48px;top:26px;font-weight:900;font-size:24px;line-height:28px;letter-spacing:.5px;color:var(--ink)}
.social{right:200px;top:28px;display:flex;gap:14px}
.social span{width:30px;height:30px;border:2px solid var(--ink);border-radius:50%;display:block}

/* hero */
.hero{left:0;top:112px;width:1200px;height:508px;background:var(--hero-bg)}
.hero-photo{left:560px;top:0;width:640px;height:508px;background:linear-gradient(120deg,#e7ecef 0%,#cfd7de 45%,#b9a89a 75%,#e9e4df 100%)}
.hero-kicker{left:152px;top:150px;font-size:25px;font-weight:500;color:var(--teal)}
.hero-title{left:152px;top:180px;font-size:48px;font-weight:900;color:var(--ink);letter-spacing:-.5px}
.hero-text{left:152px;top:246px;width:380px;font-size:12px;line-height:18px;color:var(--muted)}

/* welcome */
.welcome-photo{left:160px;top:688px;width:272px;height:376px;background:var(--white);padding:12px;box-shadow:0 6px 24px rgba(0,0,0,.18)}
.welcome-photo div{width:100%;height:100%;background:linear-gradient(160deg,#eef0f1 0%,#d3bca9 50%,#3d3d3d 100%)}
.tag{display:inline-block;background:var(--teal);color:var(--white);font-size:13px;font-weight:700;letter-spacing:1px;padding:6px 26px;border-radius:16px 4px 16px 4px}
.welcome-tag{left:596px;top:708px}
.section-title{font-weight:900;font-size:46px;color:var(--ink);letter-spacing:-.5px}
.welcome-title{left:596px;top:736px}
.welcome-sub{left:596px;top:792px;font-size:15px;color:var(--muted)}
.welcome-text{left:596px;top:826px;width:440px;font-size:12px;line-height:17px;color:var(--muted)}
.welcome-text p{margin-bottom:10px}
.feature{width:210px;text-align:center}
.feature .icon{width:56px;height:56px;margin:0 auto 10px;border:2px solid var(--teal);border-radius:50%;display:flex;align-items:center;justify-content:center}
.feature h3{font-size:16px;font-weight:500;color:var(--ink);margin-bottom:6px}
.feature p{font-size:10px;line-height:14px;color:var(--muted)}
.feature-visit{left:610px;top:1010px}
.feature-webinar{left:830px;top:1010px}

/* compare */
.compare-band{left:0;top:1284px;width:1200px;height:318px;background:var(--teal-soft)}
.compare-teal{left:0;top:1284px;width:740px;height:318px;background:var(--teal)}
.compare-title{left:152px;top:1330px;font-size:40px;font-weight:900;color:var(--white)}
.compare-list{left:160px;top:1404px;width:440px;display:grid;grid-template-columns:1fr 1fr;row-gap:16px;list-style:none}
.compare-list li{color:var(--white);font-size:12px;display:flex;align-items:center;gap:10px}
.compare-list li::before{content:"";width:12px;height:12px;border-radius:50%;background:var(--white);flex:none}
.compare-photo{top:1332px;width:216px;height:236px;background:var(--white);padding:8px;box-shadow:0 6px 20px rgba(0,0,0,.2)}
.compare-photo div{width:100%;height:100%}
.compare-before{left:580px}
.compare-before div{background:linear-gradient(170deg,#d9c9c3 0%,#2aa392 55%,#5b5b86 100%)}
.compare-after{left:816px}
.compare-after div{background:linear-gradient(170deg,#eceaea 0%,#c9a895 45%,#d9c046 100%)}

/* offer */
.offer-tag{left:0;width:1200px;top:1686px;text-align:center}
.offer-title{left:0;width:1200px;top:1716px;text-align:center;font-size:58px}
.service{top:1828px;width:208px;height:184px;border:2px solid var(--teal);display:flex;align-items:center;justify-content:center}
.service-label{top:2028px;width:208px;text-align:center;font-size:15px;line-height:20px;color:var(--ink)}
.s1{left:164px}.s2{left:384px}.s3{left:604px}.s4{left:824px}

/* contact */
.contact{left:0;top:2176px;width:1200px;height:584px;background:linear-gradient(180deg,var(--teal) 0%,var(--teal-dark) 100%)}
.contact-tag{left:0;width:1200px;top:2242px;text-align:center}
.contact-tag .tag{background:var(--white);color:var(--ink)}
.contact-title{left:0;width:1200px;top:2270px;text-align:center;font-size:58px;color:var(--white)}
.field{background:var(--white);height:44px;width:288px;font-size:11px;color:var(--muted);padding:15px 16px}
.f1{left:304px;top:2376px}.f2{left:604px;top:2376px}
.f3{left:304px;top:2436px}.f4{left:604px;top:2436px}
.message{left:304px;top:2496px;width:588px;height:112px;background:var(--white);font-size:11px;color:var(--muted);padding:15px 16px}
.submit{left:512px;top:2630px;width:176px;height:52px;border:2px solid var(--white);border-radius:26px;color:var(--white);font-weight:700;font-size:18px;display:flex;align-items:center;justify-content:center;letter-spacing:1px}

/* footer */
.site-footer{left:0;top:2760px;width:1200px;height:68px;background:var(--black);color:#bdbdbd;font-size:11px;display:flex;align-items:center;justify-content:center;letter-spacing:.5px}
</style>
</head>
<body>

<header class="site-header abs">
  <div class="brand abs">BRIGHT VITALITY<br>CENTRE</div>
  <div class="social abs"><span></span><span></span><span></span><span></span></div>
</header>

<section class="hero abs">
  <div class="hero-photo abs" role="img" aria-label="Doctor measuring a smiling woman's waist in a clinic"></div>
  <div class="hero-kicker abs">START YOUR OWN PROFITABLE</div>
  <h1 class="hero-title abs">PROFITABLE WEIGHT</h1>
  <p class="hero-text abs">We are not a weight loss franchise – you are simply buying our business model, training and support for one low fee. Please read about us, look at what we offer and compare us to weight loss franchises in the marketplace. We offer one of the easiest systems to follow. We think you will be happy you found us!</p>
</section>

<section class="welcome">
  <div class="welcome-photo abs"><div role="img" aria-label="Smiling woman measuring her waist with a tape"></div></div>
  <div class="welcome-tag abs"><span class="tag">WELCOME TO</span></div>
  <h2 class="section-title welcome-title abs">START YOUR OWN</h2>
  <div class="welcome-sub abs">Weight Loss &amp; Wellness Center</div>
  <div class="welcome-text abs">
    <p>Whether you are new, or have been in practice for years, we offer a way to add a weight loss and wellness program to your existing medical practice or open a stand-alone weight loss and wellness center.</p>
    <p>We are not a weight loss franchise – you are simply buying our business model, training and support for one low fee. Please read about us and see what we offer compared to franchises in the marketplace.</p>
    <p>We now offer one of the easiest systems to follow for your clinic. Please join our next webinar.</p>
    <p>We think you will be happy you found us!</p>
  </div>
  <div class="feature feature-visit abs">
    <div class="icon"><svg width="26" height="26" viewBox="0 0 24 24" fill="none" stroke="#17877d" stroke-width="2"><path d="M12 22s7-7 7-12a7 7 0 0 0-14 0c0 5 7 12 7 12z"/><circle cx="12" cy="10" r="2.5"/></svg></div>
    <h3>Visit Us</h3>
    <p>Schedule a visit to our clinic to see our system in action</p>
  </div>
  <div class="feature feature-webinar abs">
    <div class="icon"><svg width="26" height="26" viewBox="0 0 24 24" fill="none" stroke="#17877d" stroke-width="2"><rect x="3" y="5" width="18" height="16" rx="2"/><path d="M3 10h18M8 3v4M16 3v4"/></svg></div>
    <h3>Schedule a Webinar</h3>
    <p>Join one of our live sessions to learn more about it</p>
  </div>
</section>

<section class="compare">
  <div class="compare-band abs"></div>
  <div class="compare-teal abs"></div>
  <h2 class="compare-title abs">COMPARE</h2>
  <ul class="compare-list abs">
    <li>No franchise fees</li><li>No scope of practice limits</li>
    <li>No territory fees</li><li>No connection fees</li>
    <li>No monthly licensing fees</li><li>No % royalties</li>
    <li>No % advertising fees</li><li>No mandatory vendors</li>
  </ul>
  <div class="compare-photo compare-before abs"><div role="img" aria-label="Woman before weight loss in loose jeans"></div></div>
  <div class="compare-photo compare-after abs"><div role="img" aria-label="Slim woman after weight loss"></div></div>
</section>

<section class="offer">
  <div class="offer-tag abs"><span class="tag">WHAT</span></div>
  <h2 class="section-title offer-title abs">WE OFFER</h2>

  <div class="service s1 abs"><svg width="96" height="96" viewBox="0 0 64 64" fill="none" stroke="#17877d" stroke-width="2.5"><rect x="10" y="8" width="44" height="28"/><path d="M18 28l8-8 6 6 10-10"/><path d="M32 36v10M22 56l10-10 10 10"/></svg></div>
  <div class="service s2 abs"><svg width="96" height="96" viewBox="0 0 64 64" fill="none" stroke="#17877d" stroke-width="2.5"><rect x="6" y="10" width="52" height="34" rx="2"/><path d="M27 20v14l12-7z"/><path d="M22 54h20M32 44v10"/></svg></div>
  <div class="service s3 abs"><svg width="96" height="96" viewBox="0 0 64 64" fill="none" stroke="#17877d" stroke-width="2.5"><rect x="14" y="10" width="36" height="46" rx="2"/><rect x="24" y="6" width="16" height="8" rx="2"/><path d="M20 24l3 3 5-5M32 25h12M20 36l3 3 5-5M32 37h12M20 48h24"/></svg></div>
  <div class="service s4 abs"><svg width="96" height="96" viewBox="0 0 64 64" fill="none" stroke="#17877d" stroke-width="2.5"><rect x="12" y="14" width="40" height="26" rx="2"/><path d="M6 46h52l-4 6H10z"/><path d="M22 22h20M22 28h14"/></svg></div>

  <div class="service-label s1 abs">One-on-one business<br>&amp; medical training</div>
  <div class="service-label s2 abs">Marketing &amp;<br>Advertising Training</div>
  <div class="service-label s3 abs">Diets, Patient<br>Protocols &amp; Programs</div>
  <div class="service-label s4 abs">Office &amp; Operations<br>Manuals</div>
</section>

<section class="contact abs"></section>
<div class="contact-tag abs"><span class="tag">GET IN TOUCH</span></div>
<h2 class="section-title contact-title abs">CONTACT US</h2>
<div class="field f1 abs">Enter your name</div>
<div class="field f2 abs">Enter your phone</div>
<div class="field f3 abs">Enter your email</div>
<div class="field f4 abs">Enter your address</div>
<div class="message abs">Enter your message</div>
<div class="submit abs">SUBMIT</div>

<footer class="site-footer abs">© 2023 WWW.BRIGHTVITALITYCENTRE.COM. ALL RIGHTS RESERVED</footer>

</body>
</html>
```